Tallwater Marketing Business Card

Business card using new logo for marketing consulting company based in Silicon Valley. Limited information on card now (name, phone number, email, website), but room to add mailing address later.

```html
<!DOCTYPE html>
<html lang="en">
<head>
<meta charset="utf-8">
<title>Tallwater Marketing – Business Card</title>
<link rel="stylesheet" href="https://fonts.googleapis.com/css2?family=Open+Sans:wght@400;600;700&family=Questrial&display=swap">
<style>
  :root {
    --sky: #00aee0;
    --sky-light: #7fd6f0;
    --navy: #2e3a6e;
    --ink-grey: #8d979f;
    --text-grey: #8a9096;
    --paper: #ffffff;
    --label: #1e1e1e;
  }
  * { box-sizing: border-box; margin: 0; padding: 0; }
  html, body { width: 900px; height: 1200px; overflow: hidden; background: var(--paper); }
  .sheet {
    position: relative; width: 900px; height: 1200px;
    border: 2px solid var(--sky); background: var(--paper);
    font-family: "Open Sans", Arial, sans-serif;
  }
  .side-label {
    position: absolute; left: 62px;
    font-family: "Questrial", "Century Gothic", sans-serif;
    font-size: 34px; color: var(--label); letter-spacing: 0.5px;
  }
  .side-label--front { top: 30px; }
  .side-label--back { top: 632px; left: 66px; }

  .card { position: absolute; left: 60px; width: 783px; height: 507px; overflow: hidden; }
  .card--front { top: 83px; border: 2px solid var(--sky); background: var(--paper); }
  .card--back { top: 677px; background: var(--sky); }

  .brand { position: absolute; text-align: center; }
  .brand__dot { display: block; margin: 0 auto 14px; border-radius: 50%; background: var(--sky); }
  .brand__name {
    font-weight: 600; color: var(--sky); line-height: 1.05;
    letter-spacing: 1px; font-size: 27px;
  }
  .card--front .brand { left: 28px; top: 26px; width: 190px; }
  .card--front .brand__dot { width: 64px; height: 64px; }

  .person { position: absolute; right: 35px; top: 58px; text-align: right; }
  .person__name { font-size: 25px; font-weight: 700; color: var(--ink-grey); }
  .person__role { font-size: 22px; color: var(--navy); margin-top: 6px; letter-spacing: 0.3px; }

  .contacts { position: absolute; right: 35px; top: 255px; list-style: none; }
  .contact { display: flex; justify-content: flex-end; align-items: center; gap: 12px; height: 40px; }
  .contact__text { font-size: 20px; color: var(--text-grey); text-align: right; line-height: 31px; }
  .contact--address { align-items: flex-start; height: auto; margin-top: 2px; }
  .contact-icon { width: 31px; height: 31px; flex: none; }

  .accent-field { position: absolute; }
  .card--front .accent-field {
    left: 0; top: 255px; width: 305px; height: 252px;
    background: radial-gradient(circle at 45% 85%, var(--sky-light) 0%, rgba(127,214,240,0.35) 45%, rgba(255,255,255,0) 72%);
  }
  .card--back .accent-field {
    left: 0; top: 90px; width: 470px; height: 417px;
    background: radial-gradient(circle at 40% 60%, #bfe9f7 0%, #6fd0ef 45%, var(--sky) 78%);
  }

  .badge-disc {
    position: absolute; left: 466px; top: -2px; width: 320px; height: 320px;
    border-radius: 50%; background: var(--paper);
  }
  .card--back .brand { left: 506px; top: 66px; width: 240px; }
  .card--back .brand__dot { width: 72px; height: 72px; }
  .card--back .brand__name { font-size: 30px; }
</style>
</head>
<body>
<div class="sheet">
  <div class="side-label side-label--front">card_front</div>

  <section class="card card--front">
    <div class="brand">
      <span class="brand__dot"></span>
      <div class="brand__name">TALLWATER<br>MARKETING</div>
    </div>

    <div class="person">
      <div class="person__name">Name N. Name</div>
      <div class="person__role">DESIGNATION</div>
    </div>

    <ul class="contacts">
      <li class="contact">
        <span class="contact__text">+254 722 000 000</span>
        <svg class="contact-icon" viewBox="0 0 31 31" aria-hidden="true">
          <rect x="1" y="1" width="29" height="29" rx="6" fill="#1b7fc4"/>
          <rect x="4" y="4" width="23" height="23" rx="4" fill="#5cc7ef"/>
          <path d="M8 13c0-3 4-4 7.5-4s7.5 1 7.5 4l-2.5 1-1-2h-8l-1 2z M10 15h11l1 6H9z" fill="#fff"/>
        </svg>
      </li>
      <li class="contact">
        <span class="contact__text">+254 722 000 000</span>
        <svg class="contact-icon" viewBox="0 0 31 31" aria-hidden="true">
          <rect x="1" y="1" width="29" height="29" rx="6" fill="#1b7fc4"/>
          <rect x="4" y="4" width="23" height="23" rx="4" fill="#5cc7ef"/>
          <rect x="11" y="7" width="9" height="17" rx="2" fill="#fff"/>
          <rect x="12.5" y="9" width="6" height="5" fill="#1b7fc4"/>
        </svg>
      </li>
      <li class="contact">
        <span class="contact__text">sales@tallwater.net</span>
        <svg class="contact-icon" viewBox="0 0 31 31" aria-hidden="true">
          <rect x="1" y="1" width="29" height="29" rx="6" fill="#1b7fc4"/>
          <rect x="4" y="4" width="23" height="23" rx="4" fill="#5cc7ef"/>
          <text x="15.5" y="21" text-anchor="middle" font-family="Open Sans, sans-serif" font-size="16" font-weight="700" fill="#fff">@</text>
        </svg>
      </li>
      <li class="contact">
        <span class="contact__text">www.tallwater.net</span>
        <svg class="contact-icon" viewBox="0 0 31 31" aria-hidden="true">
          <rect x="1" y="1" width="29" height="29" rx="6" fill="#1b7fc4"/>
          <rect x="4" y="4" width="23" height="23" rx="4" fill="#5cc7ef"/>
          <circle cx="15.5" cy="15.5" r="7.5" fill="none" stroke="#fff" stroke-width="1.6"/>
          <path d="M8 15.5h15 M15.5 8c-3 4-3 11 0 15 M15.5 8c3 4 3 11 0 15" fill="none" stroke="#fff" stroke-width="1.3"/>
        </svg>
      </li>
      <li class="contact contact--address">
        <span class="contact__text">P.O. BOX 000 - 000, Silicon<br>Av, Silicon Valley</span>
        <svg class="contact-icon" viewBox="0 0 31 31" aria-hidden="true">
          <rect x="1" y="1" width="29" height="29" rx="6" fill="#1b7fc4"/>
          <rect x="4" y="4" width="23" height="23" rx="4" fill="#5cc7ef"/>
          <rect x="7" y="10" width="17" height="12" fill="#fff"/>
          <path d="M7 10l8.5 7 8.5-7" fill="none" stroke="#1b7fc4" stroke-width="1.3"/>
        </svg>
      </li>
    </ul>

    <div class="accent-field" role="img" aria-label="Decorative arrangement of sky-blue and navy circles"></div>
  </section>

  <div class="side-label side-label--back">card_back</div>

  <section class="card card--back">
    <div class="accent-field" role="img" aria-label="Decorative scatter of white circles on sky blue"></div>
    <div class="badge-disc"></div>
    <div class="brand">
      <span class="brand__dot"></span>
      <div class="brand__name">TALLWATER<br>MARKETING</div>
    </div>
  </section>
</div>
</body>
</html>
```